STOREFRONT SIGNAGE/ NEW LOGO

Looking for someone to enhance my current sign idea. I own a pawn shop , which is also a gun shop. I want a catchy front sign, which will be a lighted box sign. I may want to incorporate some symbols or character symbology that highlight firearms, such as : guns, ammo, targets, scope retical , gold, diamonds, cash, watches and/or pawn balls, and im open to other ideas, but i do not want it too busy, i want it simple, with a twist. Attached, you will find a very basic design, showing the business name and the verbiage that I would like to be incorporated into the design. God bless and thank you. may the best design win !

```html
<!DOCTYPE html>
<html lang="en">
<head>
<meta charset="utf-8">
<title>Gold &amp; Gun Exchange — Storefront Sign</title>
<link rel="stylesheet" href="https://fonts.googleapis.com/css2?family=Poppins:wght@700;800&family=Oswald:wght@500&display=swap">
<style>
  :root {
    --paper: #ffffff;
    --ink: #2a2a2a;
    --red: #e10f0f;
    --gold: #b08520;
    --gold-light: #e0b63a;
    --gold-dark: #8a6512;
    --band-dark: #262626;
  }
  * { margin: 0; padding: 0; box-sizing: border-box; }
  html, body {
    width: 866px;
    height: 1200px;
    overflow: hidden;
    background: var(--paper);
  }
  .canvas {
    position: relative;
    width: 866px;
    height: 1200px;
    display: flex;
    align-items: center;
    justify-content: center;
  }
  .sign {
    width: 780px;
    height: 227px;
    display: block;
    filter: drop-shadow(0 6px 14px rgba(0,0,0,0.28));
  }
  .headline { font-family: "Poppins", sans-serif; font-weight: 800; }
  .subline { font-family: "Poppins", sans-serif; font-weight: 700; }
  .band-text { font-family: "Poppins", sans-serif; font-weight: 700; fill: var(--paper); }
  .service { font-family: "Oswald", sans-serif; font-weight: 500; fill: var(--paper); }
  .brand-name { font-family: "Poppins", sans-serif; font-weight: 700; fill: var(--gold); }
</style>
</head>
<body>
<main class="canvas">
  <svg class="sign" viewBox="0 0 1328 387" xmlns="http://www.w3.org/2000/svg" aria-label="Gold and Gun Exchange sign">
    <defs>
      <linearGradient id="gold-sheen" x1="0" y1="0" x2="0" y2="1">
        <stop offset="0" stop-color="var(--gold-dark)"/>
        <stop offset="0.45" stop-color="var(--gold-light)"/>
        <stop offset="0.55" stop-color="var(--gold)"/>
        <stop offset="1" stop-color="var(--gold-dark)"/>
      </linearGradient>
    </defs>

    <!-- sign face -->
    <rect class="face" x="0" y="0" width="1328" height="387" fill="var(--paper)"/>

    <!-- brand block -->
    <g class="brand">
      <circle cx="150" cy="180" r="72" fill="none" stroke="var(--gold)" stroke-width="10"/>
      <text class="brand-name" x="150" y="296" font-size="34" text-anchor="middle" letter-spacing="2">MERIDIAN</text>
    </g>

    <!-- bands -->
    <polygon class="band-gold" points="297,222 812,222 812,290 269,290" fill="var(--gold)"/>
    <rect class="band-dark" x="812" y="222" width="516" height="68" fill="var(--band-dark)"/>
    <polygon class="band-red" points="269,290 1328,290 1328,387 230,387" fill="var(--red)"/>
    <polyline class="chevron" points="235,0 310,190 269,290" fill="none" stroke="var(--red)" stroke-width="5"/>

    <!-- divider and ampersand -->
    <line class="divider" x1="814" y1="0" x2="814" y2="222" stroke="var(--band-dark)" stroke-width="3"/>
    <circle class="amp-badge" cx="814" cy="122" r="67" fill="var(--band-dark)"/>
    <text class="headline" x="814" y="152" font-size="86" fill="var(--paper)" text-anchor="middle">&amp;</text>

    <!-- gold side -->
    <text class="headline" x="340" y="130" font-size="112" fill="url(#gold-sheen)" letter-spacing="-2">GOLD</text>
    <text class="subline" x="340" y="204" font-size="64" fill="var(--ink)">EXCHANGE</text>
    <text class="band-text" x="333" y="272" font-size="43">CASH FOR GOLD</text>

    <!-- gun side -->
    <text class="headline" x="1285" y="130" font-size="112" fill="var(--red)" text-anchor="end" letter-spacing="-2">GUN</text>
    <text class="subline" x="1285" y="204" font-size="64" fill="var(--ink)" text-anchor="end">EXCHANGE</text>
    <text class="band-text" x="890" y="272" font-size="43">CASH FOR GUNS</text>

    <!-- services -->
    <g class="service-dividers" stroke="rgba(0,0,0,0.25)" stroke-width="2">
      <line x1="457" y1="296" x2="457" y2="381"/>
      <line x1="647" y1="296" x2="647" y2="381"/>
      <line x1="819" y1="296" x2="819" y2="381"/>
      <line x1="1045" y1="296" x2="1045" y2="381"/>
    </g>
    <g class="ticks">
      <g transform="translate(292,334)"><circle r="12" fill="var(--paper)"/><path d="M-6 0 L-2 4 L6 -4" fill="none" stroke="var(--red)" stroke-width="3.5" stroke-linecap="round" stroke-linejoin="round"/></g>
      <g transform="translate(500,334)"><circle r="12" fill="var(--paper)"/><path d="M-6 0 L-2 4 L6 -4" fill="none" stroke="var(--red)" stroke-width="3.5" stroke-linecap="round" stroke-linejoin="round"/></g>
      <g transform="translate(682,334)"><circle r="12" fill="var(--paper)"/><path d="M-6 0 L-2 4 L6 -4" fill="none" stroke="var(--red)" stroke-width="3.5" stroke-linecap="round" stroke-linejoin="round"/></g>
      <g transform="translate(864,334)"><circle r="12" fill="var(--paper)"/><path d="M-6 0 L-2 4 L6 -4" fill="none" stroke="var(--red)" stroke-width="3.5" stroke-linecap="round" stroke-linejoin="round"/></g>
      <g transform="translate(1080,334)"><circle r="12" fill="var(--paper)"/><path d="M-6 0 L-2 4 L6 -4" fill="none" stroke="var(--red)" stroke-width="3.5" stroke-linecap="round" stroke-linejoin="round"/></g>
    </g>
    <g class="services" font-size="56">
      <text class="service" x="325" y="358">PAWN</text>
      <text class="service" x="530" y="358">BUY</text>
      <text class="service" x="705" y="358">SELL</text>
      <text class="service" x="895" y="358">TRADE</text>
      <text class="service" x="1113" y="358">LAYAWAY</text>
    </g>
  </svg>
</main>
</body>
</html>
```